Health Coaching Brochure for Healthcare Practioners

I am looking to have a tri-fold brochure created marketed towards healthcare practitioners (doctors, nurses, surgeons, etc), to get them to purchase 1-on-1 health coaching from me.
I've provided the text/content (in pdf & pages), my logo, a picture of me, and two color palettes, but please also include lots of white space. I would like to design to be very clean, modern & crisp. Also include additional photos, of doctors, etc taking care of themselves & feeling happy (maybe eating healthy, maybe exercising, feeling good & happy!)
Please also see http://brightoakwellness.com and http://instagram.com/brightoakwellness for a feel of my brand.
Thank you!
Target Market(s)
Healthcare Practioners (mainly based in Los Angeles, for now)
Industry/Entity Type
Healthcare
Look and feel

```html
<!DOCTYPE html>
<html lang="en">
<head>
<meta charset="utf-8">
<title>Holistic Health Coaching for Healthcare Practitioners – Tri-fold Brochure</title>
<link href="https://fonts.googleapis.com/css2?family=Montserrat:wght@400;500;600;700&family=Oswald:wght@600;700&display=swap" rel="stylesheet">
<style>
:root{
  --navy:#1d4f8c;
  --blue:#5b93c9;
  --cyan:#1cb3e6;
  --ink:#333a40;
  --rule:#8cc5e8;
  --paper:#ffffff;
  --backdrop:#d5d5d5;
}
*{margin:0;padding:0;box-sizing:border-box}
html,body{width:1200px;height:1200px;overflow:hidden;background:var(--backdrop)}
body{font-family:"Montserrat",Arial,sans-serif;color:var(--ink)}
.stage{position:absolute;left:0;top:0;width:1500px;height:1500px;transform:scale(.8);transform-origin:0 0}
.sheet{position:absolute;left:315px;width:870px;height:676px;background:var(--paper);overflow:hidden}
.sheet--outside{top:51px}
.sheet--inside{top:767px}
.abs{position:absolute}
.photo{position:absolute;overflow:hidden}
.dot{position:absolute;border-radius:50%}

/* outside – left flap */
.flap-title{left:19px;top:21px;width:266px;border-top:2px solid var(--rule);border-bottom:2px solid var(--rule);padding:4px 0 3px;color:var(--navy);font-weight:700;font-size:15px;line-height:20px;letter-spacing:.2px}
.lead{left:19px;top:75px;width:250px;font-size:13px;font-weight:500;line-height:16px;color:#333}
.bullets{left:19px;top:129px;width:250px;list-style:none;font-size:10.3px;line-height:13px;color:#444}
.bullets li{position:relative;padding-left:10px;margin-bottom:7.5px}
.bullets li::before{content:"";position:absolute;left:0;top:5px;width:4px;height:4px;border-radius:50%;background:var(--cyan)}
.closing{left:19px;top:307px;width:250px;font-size:12.5px;font-weight:600;line-height:16px;color:#333}

/* outside – middle panel */
.mid{left:283px;top:0;width:288px;height:676px;background:var(--blue)}
.bio{left:14px;top:215px;width:240px;color:#fff;font-size:10.4px;line-height:13px;text-align:justify;text-align-last:center}
.cta{left:0;top:315px;width:288px;text-align:center;color:#fff;font-weight:600;font-size:26px;line-height:31.5px;letter-spacing:1.2px}
.icon{position:absolute;width:20px;height:20px;border-radius:50%;background:var(--navy)}
.phone{left:0;top:479px;width:276px;text-align:center;color:#fff;font-size:22px;font-weight:500;letter-spacing:.6px}
.site{left:0;top:544px;width:288px;text-align:center;color:#fff;font-size:11px;letter-spacing:1.5px}

/* outside – cover */
.cover-kicker{left:571px;top:474px;width:299px;text-align:center;color:var(--navy);font-weight:700;font-size:18px;letter-spacing:.6px}
.cover-big{left:571px;width:299px;text-align:center;color:var(--navy);font-family:"Oswald",Impact,sans-serif;font-weight:700;line-height:1}
.cover-mid{left:571px;top:549px;width:299px;text-align:center;color:var(--navy);font-weight:600;font-size:17px;letter-spacing:.6px}
.cover-site{left:605px;top:636px;width:230px;text-align:center;font-size:11px;letter-spacing:2.2px;color:var(--navy);border-bottom:2px solid var(--rule);padding-bottom:6px}

/* inside – left */
.take{left:22px;top:176px;font-size:17px;font-weight:600;color:#555}
.care{left:22px;top:196px;font-size:31px;font-weight:700;color:var(--navy);letter-spacing:.5px}
.deserve{left:22px;top:244px;width:186px;font-size:24px;color:#444;border-top:2px solid var(--rule);border-bottom:2px solid var(--rule);padding:2px 0 2px 2px}
.ready{left:22px;top:288px;color:var(--navy);font-weight:700;line-height:1}
.talk{left:20px;top:405px;font-size:28px;font-weight:500;color:#222}
.schedule{left:21px;top:443px;width:260px;font-size:16.5px;font-weight:500;color:var(--navy);line-height:24px}
.contact{left:18px;top:560px;font-size:15px;font-weight:500;color:#222}
.contact-list{left:18px;top:588px;list-style:none;font-size:13px;font-weight:500;color:#222;line-height:21px}
.contact-list li{display:flex;align-items:center;gap:7px}
.mini{width:9px;height:9px;border-radius:50%;background:var(--navy);flex:none}

/* inside – middle */
.sec-title{left:311px;color:var(--navy);font-weight:700;font-size:17px;border-top:2px solid var(--rule);border-bottom:2px solid var(--rule);padding:2px 2px}
.checks{left:313px;width:240px;list-style:none;font-size:11px;line-height:13px;color:#444}
.checks li{position:relative;padding-left:21px;margin-bottom:6.5px}
.checks li svg{position:absolute;left:0;top:1px}

/* inside – right */
.testi-title{left:592px;top:24px;width:262px;text-align:center;font-weight:700;font-size:18px;color:#333;letter-spacing:.5px}
.quote-rule{position:absolute;height:2px;background:var(--rule)}
.qmark{position:absolute;color:var(--cyan);font-family:Georgia,serif;font-weight:700;font-size:22px;line-height:1}
.testi{left:593px;width:252px;font-size:9.4px;line-height:11.8px;color:#444;text-align:justify}
.testi p{margin-bottom:6px}
.sign{position:absolute;font-size:9.6px;font-weight:700;font-style:italic;color:var(--navy)}
.sign::before{content:"";display:inline-block;width:28px;height:1px;background:#999;vertical-align:middle;margin-right:5px}
</style>
</head>
<body>
<div class="stage">

  <!-- OUTSIDE SHEET -->
  <section class="sheet sheet--outside">
    <!-- left flap -->
    <h2 class="abs flap-title">HEALTH COACHING FOR<br>HEALTHCARE PRACTIONERS</h2>
    <p class="abs lead">Are you overwhelmed and exhausted and feel like there’s no time left for YOU?</p>
    <ul class="abs bullets">
      <li>Do you put everyone and everything else before your own health?</li>
      <li>Are you struggling with how to fit in exercise after working 12-15 hour shifts?</li>
      <li>Do you know exactly what you should do to take care of yourself, but it’s just not happening?</li>
      <li>Have you gained weight due to stress-eating, and ready to take it off?</li>
      <li>Are you ready to feel energetic and sexy and to fully love yourself again?</li>
    </ul>
    <p class="abs closing">As healthcare practitioners, it’s easy to lose sight of your own wants and needs, when you’re so busy taking care of everyone else.</p>

    <div class="photo" style="left:0;top:390px;width:313px;height:300px;border-radius:0 300px 0 0;background:linear-gradient(160deg,#e9eef3 0%,#b9cfe6 45%,#3f7fc8 100%)" role="img" aria-label="Nurse in blue scrubs meditating cross-legged in a hospital corridor"></div>
    <div class="dot" style="left:-30px;top:390px;width:90px;height:90px;background:var(--blue);opacity:.85"></div>
    <div class="dot" style="left:255px;top:611px;width:93px;height:93px;background:var(--paper)"></div>

    <!-- middle panel -->
    <div class="abs mid">
      <div class="photo" style="left:70px;top:59px;width:130px;height:130px;border-radius:50%;background:radial-gradient(circle at 50% 40%,#e7d2c4 0%,#a27a66 55%,#4b3a33 100%)" role="img" aria-label="Portrait of the health coach"></div>
      <div class="dot" style="left:67px;top:153px;width:50px;height:50px;background:var(--cyan)"></div>
      <p class="abs bio">Maya Ortega is a personal trainer, fitness nutritionist, and holistic health coach based in Los Angeles, California. Maya helps clients improve their health, develop sustainable habits, and achieve their goals to be their best, most vibrant selves.</p>
      <h3 class="abs cta">CALL FOR<br>YOUR FREE<br>15 MINUTE<br>CONSULTATION</h3>
      <span class="icon" style="left:120px;top:451px">
        <svg width="20" height="20" viewBox="0 0 20 20"><path d="M7 5.5l1.6 2.2-1 1c.6 1.3 1.5 2.2 2.8 2.8l1-1 2.2 1.6-.8 1.6c-3.6-.3-6.3-3-6.6-6.6z" fill="#fff"/></svg>
      </span>
      <p class="abs phone">1 310-555-0147</p>
      <span class="icon" style="left:120px;top:515px">
        <svg width="20" height="20" viewBox="0 0 20 20" fill="none" stroke="#fff" stroke-width="1.1"><circle cx="10" cy="10" r="4.5"/><path d="M5.5 10h9M10 5.5c-2 2.5-2 6.5 0 9M10 5.5c2 2.5 2 6.5 0 9"/></svg>
      </span>
      <p class="abs site">www.brightoakwellness.com</p>
    </div>

    <!-- cover -->
    <svg class="abs" style="left:535px;top:0" width="335" height="400" viewBox="0 0 335 400" aria-hidden="true">
      <path d="M36 0 H335 V380 C300 395 230 395 190 370 C120 330 40 300 20 230 C0 160 10 60 36 0Z" fill="#eef2f6"/>
    </svg>
    <div class="photo" style="left:548px;top:40px;width:322px;height:345px;border-radius:160px 0 0 60px;background:linear-gradient(180deg,#f1f4f7 0%,#dbe7f1 40%,#6fa5d6 75%,#3d7fbf 100%)" role="img" aria-label="Group of smiling doctors and nurses in scrubs and white coats"></div>
    <div class="photo" style="left:553px;top:255px;width:190px;height:190px;border-radius:50%;border:6px solid #fff;background:radial-gradient(circle at 50% 45%,#f4e4d9 0%,#d9d3cc 45%,#eef0f0 100%)" role="img" aria-label="Smiling female doctor holding a green apple and stethoscope"></div>
    <div class="dot" style="left:706px;top:367px;width:80px;height:80px;background:var(--cyan)"></div>

    <p class="abs cover-kicker">HOLISTIC HEALTH</p>
    <p class="abs cover-big" style="top:496px;font-size:49px;letter-spacing:.5px">COACHING</p>
    <p class="abs cover-mid">FOR HEALTHCARE</p>
    <p class="abs cover-big" style="top:573px;font-size:47px">PRACTIONERS</p>
    <p class="abs cover-site">www.brightoakwellness.com</p>
  </section>

  <!-- INSIDE SHEET -->
  <section class="sheet sheet--inside">
    <!-- left -->
    <div class="photo" style="left:-130px;top:-230px;width:760px;height:375px;border-radius:0 0 50% 50%;background:linear-gradient(135deg,#3f7fc4 0%,#86b4de 45%,#c9def0 80%)" role="img" aria-label="Close-up of clear water and ice in cool blue tones"></div>
    <div class="dot" style="left:340px;top:-20px;width:86px;height:86px;background:#4f86c0;opacity:.9"></div>
    <div class="dot" style="left:-10px;top:78px;width:70px;height:70px;background:#3e78b8;opacity:.7"></div>

    <p class="abs take">It’s time to take</p>
    <p class="abs care">CARE OF YOU!</p>
    <p class="abs deserve">You deserve it!</p>
    <p class="abs ready"><span style="font-size:32px">Are you ready</span><br><span style="font-size:22px;line-height:30px;font-weight:600">for a</span><br><span style="font-size:31px;font-weight:600;letter-spacing:.8px">CHANGE?</span></p>
    <p class="abs talk">Let’s talk!</p>
    <p class="abs schedule">SCHEDULE your 15 minute consultation today<br>to discuss your unique situation and your goals.</p>
    <p class="abs contact">Contact</p>
    <ul class="abs contact-list">
      <li><span class="mini"></span>brightoakwellness.com</li>
      <li><span class="mini"></span>maya@brightoakwellness.com</li>
      <li><span class="mini"></span>310.555.0147</li>
    </ul>

    <!-- middle -->
    <h3 class="abs sec-title" style="top:113px">How would it feel if...</h3>
    <ul class="abs checks" style="top:152px">
      <li><svg width="11" height="11" viewBox="0 0 11 11" fill="none" stroke="#1cb3e6" stroke-width="1.3"><circle cx="5.5" cy="5.5" r="4.6"/><path d="M3.2 5.6l1.6 1.5 3-3"/></svg>You woke up everyday feeling energized and ready to tackle the day?</li>
      <li><svg width="11" height="11" viewBox="0 0 11 11" fill="none" stroke="#1cb3e6" stroke-width="1.3"><circle cx="5.5" cy="5.5" r="4.6"/><path d="M3.2 5.6l1.6 1.5 3-3"/></svg>You felt calm and clear-headed?</li>
      <li><svg width="11" height="11" viewBox="0 0 11 11" fill="none" stroke="#1cb3e6" stroke-width="1.3"><circle cx="5.5" cy="5.5" r="4.6"/><path d="M3.2 5.6l1.6 1.5 3-3"/></svg>You were in control of your food choices and cravings?</li>
      <li><svg width="11" height="11" viewBox="0 0 11 11" fill="none" stroke="#1cb3e6" stroke-width="1.3"><circle cx="5.5" cy="5.5" r="4.6"/><path d="M3.2 5.6l1.6 1.5 3-3"/></svg>You dropped the weight and fell in love with your life again?</li>
      <li><svg width="11" height="11" viewBox="0 0 11 11" fill="none" stroke="#1cb3e6" stroke-width="1.3"><circle cx="5.5" cy="5.5" r="4.6"/><path d="M3.2 5.6l1.6 1.5 3-3"/></svg>You felt like yourself again?</li>
      <li><svg width="11" height="11" viewBox="0 0 11 11" fill="none" stroke="#1cb3e6" stroke-width="1.3"><circle cx="5.5" cy="5.5" r="4.6"/><path d="M3.2 5.6l1.6 1.5 3-3"/></svg>You had the support and accountability to reach your goals?</li>
    </ul>
    <h3 class="abs sec-title" style="top:344px">Services include:</h3>
    <ul class="abs checks" style="top:387px">
      <li><svg width="11" height="11" viewBox="0 0 11 11" fill="none" stroke="#1cb3e6" stroke-width="1.3"><circle cx="5.5" cy="5.5" r="4.6"/><path d="M3.2 5.6l1.6 1.5 3-3"/></svg>1-on-1 Virtual Health Coaching</li>
      <li><svg width="11" height="11" viewBox="0 0 11 11" fill="none" stroke="#1cb3e6" stroke-width="1.3"><circle cx="5.5" cy="5.5" r="4.6"/><path d="M3.2 5.6l1.6 1.5 3-3"/></svg>Virtual Group Coaching</li>
      <li><svg width="11" height="11" viewBox="0 0 11 11" fill="none" stroke="#1cb3e6" stroke-width="1.3"><circle cx="5.5" cy="5.5" r="4.6"/><path d="M3.2 5.6l1.6 1.5 3-3"/></svg>Custom Workout Program and/or Meal Plan</li>
      <li><svg width="11" height="11" viewBox="0 0 11 11" fill="none" stroke="#1cb3e6" stroke-width="1.3"><circle cx="5.5" cy="5.5" r="4.6"/><path d="M3.2 5.6l1.6 1.5 3-3"/></svg>Grocery Store Tour</li>
      <li><svg width="11" height="11" viewBox="0 0 11 11" fill="none" stroke="#1cb3e6" stroke-width="1.3"><circle cx="5.5" cy="5.5" r="4.6"/><path d="M3.2 5.6l1.6 1.5 3-3"/></svg>Pantry Clean Out</li>
      <li><svg width="11" height="11" viewBox="0 0 11 11" fill="none" stroke="#1cb3e6" stroke-width="1.3"><circle cx="5.5" cy="5.5" r="4.6"/><path d="M3.2 5.6l1.6 1.5 3-3"/></svg>Personal Training Also Available (in the Glendale area)</li>
    </ul>
    <div class="photo" style="left:360px;top:530px;width:180px;height:180px;border-radius:50%;background:radial-gradient(circle at 50% 40%,#f6f6f6 0%,#e6ecf2 55%,#c9d9ea 100%)" role="img" aria-label="Cheerful group of doctors in white coats raising their arms"></div>
    <div class="dot" style="left:420px;top:636px;width:80px;height:80px;background:#3d78bd"></div>

    <!-- right -->
    <h3 class="abs testi-title">TESTIMONIALS</h3>
    <span class="qmark" style="left:593px;top:50px">“</span>
    <span class="quote-rule" style="left:615px;top:58px;width:207px"></span>
    <div class="abs testi" style="top:71px">
      <p>I’m a physician by profession and over the past few years- work stress, bad lifestyle choices, bad diet &amp; poor sleep patterns, finally started to catch up. When I met Maya about 8 months ago, my physical and mental health was in terrible shape.</p>
      <p>As a personal trainer- Maya knows what she is doing, training sessions are personalized to my individual goals, she is polite/supportive but she can also be strict! She knows how to keep me motivated, how to push me to my limits. I can actually do one legged squats, who knew!</p>
      <p>As a health coach - Maya has wealth of knowledge! Being a physician, I always thought I knew enough about healthy diet, healthier lifestyle &amp; I couldn’t be more wrong! I have learnt so much from her; my diet is completely changed (in a good way), I love what I eat, I sleep better, I can think more clearly. Overall, I feel healthier &amp; happier.</p>
    </div>
    <span class="sign" style="left:756px;top:292px">Devin K</span>
    <span class="quote-rule" style="left:593px;top:316px;width:210px"></span>
    <span class="qmark" style="left:808px;top:308px">”</span>

    <span class="qmark" style="left:593px;top:324px">“</span>
    <span class="quote-rule" style="left:615px;top:333px;width:207px"></span>
    <div class="abs testi" style="top:346px">
      <p>Maya has been my trainer for the last 7 years and I can’t recommend her highly enough. She makes exercise fun and i look forward to our sessions! I am a mother of 2 young children and work full time as an ER doctor, both of which can be physically and emotionally draining. She has helped me stay healthy and strong with excellent physical fitness training and nutritional coaching.</p>
    </div>
    <span class="sign" style="left:710px;top:442px">Priya M</span>
    <span class="quote-rule" style="left:593px;top:466px;width:210px"></span>
    <span class="qmark" style="left:808px;top:456px">”</span>

    <div class="photo" style="left:555px;top:498px;width:315px;height:178px;background:linear-gradient(120deg,#f3f6f8 0%,#e3edf3 40%,#d4e5ef 70%,#f0f2f3 100%)" role="img" aria-label="Smiling doctor and woman sharing a healthy meal with fruit and juice"></div>
    <div class="dot" style="left:813px;top:556px;width:60px;height:60px;background:var(--cyan)"></div>
  </section>

</div>
</body>
</html>
```